Business Card Design Project

We are looking for a new business card design for a Drilling company in WA, Australia.

We are in between offices, however require a design in the meantime due to some upcoming events with our basic information.

The Logo for our company is Blue and Grey and would like this colour scheme throughout.

We are quite a new company so would like a memorable design that stands out and communicates a strong commitment to safety, quality of work and performance.

The company name is Ridgeback Boring Works (RBW)

The details to be included are as follows:

Martin Calloway
Managing Director
m.0481639027
e.martin@rbwgroup.com.au

Simon Calloway
Director
m.0429561384
e.simon@rbwgroup.com.au

Industry/Entity Type

Events

Requirements
Must have
• Under the Logo, we would like 'Western Australia'

```html
<!DOCTYPE html>
<html lang="en">
<head>
<meta charset="utf-8">
<title>Ridgeback Boring Works – Business Card</title>
<link rel="stylesheet" href="https://fonts.googleapis.com/css2?family=Open+Sans:wght@400;600&display=swap">
<style>
  :root {
    --brand-blue: #1c3f8c;
    --brand-grey: #7a7a7a;
    --text-grey: #6b6b6b;
    --card-white: #ffffff;
    --backdrop: #e4e8ea;
    --rule-grey: #c8c8c8;
  }
  * { margin: 0; padding: 0; box-sizing: border-box; }
  html, body {
    width: 1200px; height: 960px; overflow: hidden;
    background: var(--backdrop);
    font-family: "Open Sans", Arial, sans-serif;
  }
  .stage {
    width: 1200px; height: 960px;
    display: flex; flex-direction: column; align-items: center; justify-content: center;
    gap: 60px;
  }
  .card {
    position: relative;
    width: 580px; height: 340px;
    background: var(--card-white);
    box-shadow: 0 4px 14px rgba(0,0,0,0.12);
  }

  /* Front */
  .card-front .brand {
    position: absolute; left: 70px; top: 112px;
    display: flex; align-items: center; gap: 16px;
  }
  .brand-square {
    width: 22px; height: 22px; background: var(--brand-blue);
  }
  .brand-name {
    font-size: 34px; font-weight: 600; color: var(--brand-blue);
    letter-spacing: 0.5px; line-height: 1;
  }
  .card-front .region {
    position: absolute; right: 70px; top: 178px;
    font-size: 20px; color: var(--text-grey);
  }

  /* Back */
  .card-back .brand {
    position: absolute; left: 34px; top: 62px;
    display: flex; align-items: center; gap: 10px;
  }
  .card-back .brand-square { width: 14px; height: 14px; }
  .card-back .brand-name { font-size: 20px; }
  .card-back .divider {
    position: absolute; left: 34px; right: 0; top: 128px;
    height: 3px; background: var(--brand-blue);
  }
  .contact {
    position: absolute; left: 400px; top: 70px;
    color: var(--text-grey);
  }
  .contact .person {
    font-size: 16px; letter-spacing: 1.5px; text-transform: uppercase;
  }
  .contact .role { font-size: 15px; margin-top: 2px; }
  .contact .lines {
    list-style: none; margin-top: 42px; font-size: 12px; line-height: 1.7;
  }
  .contact .label { color: var(--brand-blue); font-weight: 600; display: inline-block; width: 12px; }
</style>
</head>
<body>
  <main class="stage">
    <section class="card card-front">
      <div class="brand">
        <span class="brand-square"></span>
        <span class="brand-name">Ridgeback Boring Works</span>
      </div>
      <p class="region">Western Australia</p>
    </section>

    <section class="card card-back">
      <div class="brand">
        <span class="brand-square"></span>
        <span class="brand-name">Ridgeback Boring Works</span>
      </div>
      <div class="divider"></div>
      <div class="contact">
        <p class="person">Martin Calloway</p>
        <p class="role">Managing Director</p>
        <ul class="lines">
          <li><span class="label">m</span>: 0481639027</li>
          <li><span class="label">e</span>: martin@rbwgroup.com.au</li>
        </ul>
      </div>
    </section>
  </main>
</body>
</html>
```